Fresh Nest Builder Guide needs a new Landing Page

I like to get a landing page or website with 2-3 pages to help target home buyers who are looking to buy homes from builders such as PV Dwellings, Moritz, G.T. Falwick, etc. The landing page/website to be non-cluttered and be able to explain to home buyers that there are many benefits to include me as their buyer's agent when they buy a brand new home from any builders.
I may want to incorporate a short explanation video (animated) on the landing page and then for the viewer to click on a button that will take them to another page where they can search for new homes from different builders.
Target Market(s)
Home buyers looking to buy brand new home from builders such as PV Dwellings, Moritz, G.T. Falwick, etc.
Industry/Entity Type
Real Estate
Number of Pages Required
2 page
Requirements
Must have
- The landing page may have the explanation video at the bottom of the landing page (scrolled down) or there may be a CALL TO ACTION button that takes the viewer to the 2nd page to watch the explanation video. Once they watched the explanation video and are still interested, they can click on another CALL TO ACTION button that will take them to another website that they will be able to search for all the available new homes and register their contact information.
Should not have
- No clutters and no dark colors.

```html
<!DOCTYPE html>
<html lang="en">
<head>
<meta charset="utf-8">
<title>Fresh Nest Builder Guide</title>
<link href="https://fonts.googleapis.com/css2?family=Noto+Serif:ital,wght@0,700;1,700&family=Jost:wght@400;500;600&display=swap" rel="stylesheet">
<style>
:root{
  --brown:#5c4a32;
  --brown-dark:#4a3b27;
  --orange:#d6501c;
  --gold:#b08a2c;
  --ink:#1f1f1f;
  --muted:#555;
  --line:#dcdcdc;
  --soft:#f5f5f5;
  --panel:#efefef;
  --cream:#f3ece2;
  --sand:#e6dccd;
  --white:#fff;
}
*{box-sizing:border-box;margin:0;padding:0}
html,body{width:1200px;height:3516px;overflow:hidden}
body{position:relative;font-family:"Jost",sans-serif;color:var(--ink);background:var(--white)}
.abs{position:absolute}

/* hero */
.hero{left:0;top:0;width:1200px;height:558px;background:linear-gradient(160deg,#efe4d4 0%,#e2d3bd 45%,#d9cbb6 75%,#cdbfaa 100%)}
.brand{left:500px;top:33px;width:203px;height:112px;background:var(--white);border-radius:8px;display:flex;flex-direction:column;align-items:center;justify-content:center;gap:8px;box-shadow:0 2px 10px rgba(0,0,0,.08)}
.brand-dot{width:30px;height:30px;border-radius:50%;background:var(--brown)}
.brand-name{font-size:19px;font-weight:500;color:var(--brown);text-align:center;line-height:1.1}
.quote{left:60px;top:196px;width:640px;font-family:"Noto Serif",serif;font-style:italic;font-weight:700;font-size:42px;line-height:1.3;color:var(--brown-dark);text-align:right;white-space:nowrap}
.badge{left:720px;top:183px;width:68px;height:68px;border-radius:50%;background:var(--orange);color:var(--white);text-align:center;font-weight:600;font-size:24px;line-height:1;padding-top:16px}
.badge small{display:block;font-size:10px;letter-spacing:1px}
.starting{left:727px;top:256px;font-size:12px;letter-spacing:2px;color:var(--gold);font-weight:600}
.price-range{left:727px;top:270px;font-size:29px;font-weight:600;color:var(--brown-dark)}
.hero-note{left:727px;top:311px;width:360px;font-size:12px;letter-spacing:1.2px;color:#4a4033;text-transform:uppercase;line-height:1.5}
.lead-form{left:87px;top:391px;width:1026px;height:129px;background:var(--white);border-radius:4px;box-shadow:0 4px 18px rgba(0,0,0,.12)}
.field{position:absolute;top:31px}
.field label{display:block;font-size:14px;font-weight:600;margin-bottom:7px}
.field label b{color:var(--orange)}
.field span{display:block;height:35px;border:1px solid #cfcfcf;background:#fafafa}
.submit{position:absolute;left:848px;top:54px;width:134px;height:35px;background:var(--brown-dark);color:var(--white);font-size:12px;font-weight:600;letter-spacing:1.5px;display:flex;align-items:center;justify-content:center}
.scroll-down{left:582px;top:540px;width:36px;height:36px;border-radius:50%;background:var(--white);box-shadow:0 2px 8px rgba(0,0,0,.2);display:flex;align-items:center;justify-content:center}

/* section headings */
.sec-head{left:0;width:1200px;text-align:center}
.sec-title{display:inline-flex;align-items:center;gap:14px;font-family:"Noto Serif",serif;font-weight:700;font-size:28px;color:var(--brown)}
.sec-title i{display:block;width:70px;height:2px;background:var(--brown);position:relative}
.sec-title i::after{content:"";position:absolute;top:-4px;width:10px;height:10px;border-radius:50%;border:2px solid var(--brown);background:var(--white)}
.sec-title i.l::after{right:-4px}
.sec-title i.r::after{left:-4px}
.sec-desc{margin:14px auto 0;width:460px;font-size:14px;line-height:1.55;color:var(--ink)}

/* features */
.feature{top:743px;width:235px;height:129px;background:var(--panel);border:1px solid #e2e2e2;display:flex;flex-direction:column;align-items:center;justify-content:center;gap:14px;font-size:16px}
.feature .ico{width:44px;height:44px;border-radius:50%;border:2px solid #666;display:flex;align-items:center;justify-content:center}
.pager{left:0;width:1200px;display:flex;justify-content:center;align-items:center;gap:28px;font-size:10px;font-weight:600;letter-spacing:1px}
.pager .dots{display:flex;gap:6px;align-items:center}
.pager .dots span{width:5px;height:5px;border-radius:50%;background:#aaa}
.pager .dots span.on{width:9px;height:9px;border:2px solid #888;background:transparent}

/* stats */
.stats{left:0;top:980px;width:1200px;height:211px;background:linear-gradient(180deg,var(--cream),var(--sand))}
.stat{top:1060px;display:flex;align-items:center;gap:16px;color:var(--brown-dark)}
.stat .ic{width:48px;height:48px;border-radius:50%;border:2px solid var(--brown);display:flex;align-items:center;justify-content:center}
.stat em{display:block;font-style:normal;font-size:11px;letter-spacing:1.5px;color:var(--gold);text-transform:uppercase}
.stat strong{display:block;font-weight:400;font-size:36px;line-height:1}

/* listings */
.listing{left:0;top:1191px;width:1200px;height:1165px;background:var(--soft)}
.card{width:323px;height:401px;background:var(--white);border:1px solid #e3e3e3}
.card .photo{height:174px}
.card .tag{position:absolute;left:20px;top:149px;width:80px;height:38px;background:var(--orange);color:var(--white);font-weight:600;font-size:18px;display:flex;align-items:center;justify-content:center}
.card h3{position:absolute;left:18px;top:200px;font-size:19px;font-weight:500}
.card .sub{position:absolute;left:18px;top:226px;font-size:13px;color:var(--muted)}
.card .spec{position:absolute;font-size:12px;display:flex;align-items:center;gap:8px}
.card .foot{position:absolute;left:0;bottom:0;width:100%;height:44px;border-top:1px solid #e3e3e3;display:flex}
.card .foot .agent{flex:1;display:flex;align-items:center;gap:10px;padding-left:16px;font-size:13px}
.card .foot .btn{width:44px;border-left:1px solid #e3e3e3;display:flex;align-items:center;justify-content:center}
.view-more{left:523px;top:2243px;width:154px;height:45px;background:var(--brown);border:2px solid #3b2f20;color:var(--white);font-size:12px;font-weight:600;letter-spacing:1.5px;display:flex;align-items:center;justify-content:center;gap:8px}

/* why choose */
.video{left:87px;top:2541px;width:499px;height:265px;background:linear-gradient(135deg,#e4ddd4,#c9bfb3 60%,#a99e92);display:flex;flex-direction:column;align-items:center;justify-content:center;gap:10px;color:var(--white);font-size:17px}
.video .play{width:40px;height:40px;border-radius:50%;border:2px solid var(--white);display:flex;align-items:center;justify-content:center}
.why-title{left:630px;top:2588px;font-size:25px;font-weight:500}
.why-text{left:630px;top:2630px;width:480px;font-size:13.5px;line-height:1.55}
.metric{top:2712px;display:flex;align-items:center;gap:12px;font-size:12px;letter-spacing:1px;text-transform:uppercase;line-height:1.3}
.metric .ic{width:40px;height:40px;border-radius:50%;border:2px solid #555;display:flex;align-items:center;justify-content:center}
.metric b{display:block;font-size:12px}

/* testimonial */
.testimonial{left:0;top:2876px;width:1200px;height:312px;background:linear-gradient(100deg,#f1e2d8 0%,#ece4da 45%,#e4ddd3 100%)}
.avatar{left:556px;top:2920px;width:88px;height:88px;border-radius:50%;background:#b9c0c6;border:4px solid var(--white)}
.t-name{left:0;top:3020px;width:1200px;text-align:center;color:var(--brown-dark);font-size:16px;font-weight:600;letter-spacing:1px}
.t-stars{left:0;top:3042px;width:1200px;text-align:center;color:var(--gold);font-size:11px;letter-spacing:2px}
.t-text{left:350px;top:3062px;width:500px;text-align:center;color:#333;font-size:14px;line-height:1.55}

/* footer */
.footer{left:0;top:3188px;width:1200px;height:281px;background:var(--white)}
.f-title{font-size:23px;font-weight:500}
.f-text{font-size:13.5px;line-height:1.55}
.subscribe{left:87px;top:3366px;width:323px;height:34px;border:1px solid #ccc;background:#f6f6f6;display:flex;align-items:center;font-size:12px;color:#777}
.subscribe span{flex:1;padding-left:12px}
.subscribe i{width:50px;height:100%;border-left:1px solid #ccc;display:flex;align-items:center;justify-content:center}
.contact{top:3296px;display:flex;align-items:center;gap:14px}
.contact em{display:block;font-style:normal;font-size:11px}
.contact strong{display:block;font-weight:400;font-size:17px}
.social{top:3366px;width:32px;height:32px;border-radius:50%;background:#ebebeb}
.bottom-bar{left:0;top:3469px;width:1200px;height:47px;background:var(--cream);color:#6a5d4b;font-size:11px;display:flex;align-items:center;justify-content:center;letter-spacing:.5px}
.bottom-bar b{color:var(--brown-dark);letter-spacing:1.5px;margin:0 4px}
</style>
</head>
<body>

<!-- hero -->
<section class="abs hero" role="img" aria-label="Bright daytime photo of a new modern home"></section>
<div class="abs brand"><span class="brand-dot"></span><span class="brand-name">Fresh Nest<br>Builder Guide</span></div>
<h1 class="abs quote">“Everyone Deserves<br>the Opportunity of Home”</h1>
<div class="abs badge">32%<small>OFF</small></div>
<div class="abs starting">STARTING AT</div>
<div class="abs price-range">$270 - $3,484</div>
<p class="abs hero-note">The builder pays your agent's fee, so expert help costs you nothing.</p>

<form class="abs lead-form">
  <div class="field" style="left:42px;width:155px"><label>First name <b>*</b></label><span></span></div>
  <div class="field" style="left:215px;width:155px"><label>Last name <b>*</b></label><span></span></div>
  <div class="field" style="left:389px;width:152px"><label>Phone number <b>*</b></label><span></span></div>
  <div class="field" style="left:562px;width:261px"><label>Email address <b>*</b></label><span></span></div>
  <div class="submit">SUBMIT NOW</div>
</form>
<div class="abs scroll-down"><svg width="12" height="8" viewBox="0 0 12 8"><path d="M1 1l5 5 5-5" fill="none" stroke="#333" stroke-width="2"/></svg></div>

<!-- why special -->
<header class="abs sec-head" style="top:620px">
  <h2 class="sec-title"><i class="l"></i>Why we are special<i class="r"></i></h2>
  <p class="sec-desc">A buyer's agent works only for you when you buy a brand new home from any builder.</p>
</header>
<div class="abs feature" style="left:218px"><span class="ico"><svg width="18" height="18"><rect x="3" y="3" width="12" height="12" fill="none" stroke="#555" stroke-width="2"/></svg></span>Free Representation</div>
<div class="abs feature" style="left:482px"><span class="ico"><svg width="18" height="18"><path d="M3 9l4 4 8-9" fill="none" stroke="#555" stroke-width="2"/></svg></span>Expert Negotiation</div>
<div class="abs feature" style="left:745px"><span class="ico"><svg width="20" height="20"><circle cx="10" cy="10" r="7" fill="none" stroke="#555" stroke-width="2"/><path d="M10 3v14M3 10h14" stroke="#555" stroke-width="1.5"/></svg></span>Builder Know-how</div>
<div class="abs pager" style="top:895px;color:#333"><span>⟵ PRE</span><span class="dots"><span></span><span class="on"></span><span></span></span><span>NEX ⟶</span></div>

<!-- stats -->
<section class="abs stats" role="img" aria-label="Soft light photo of a new house"></section>
<div class="abs stat" style="left:253px"><span class="ic"><svg width="24" height="24"><circle cx="12" cy="12" r="9" fill="none" stroke="#5c4a32" stroke-width="2"/><path d="M8 14q4 4 8 0" fill="none" stroke="#5c4a32" stroke-width="2"/><circle cx="9" cy="9" r="1.3" fill="#5c4a32"/><circle cx="15" cy="9" r="1.3" fill="#5c4a32"/></svg></span><div><em>Happy customer</em><strong>1500</strong></div></div>
<div class="abs stat" style="left:516px"><span class="ic"><svg width="24" height="24"><circle cx="12" cy="9" r="4" fill="none" stroke="#5c4a32" stroke-width="2"/><path d="M4 21q8-10 16 0" fill="none" stroke="#5c4a32" stroke-width="2"/></svg></span><div><em>Our agents</em><strong>424</strong></div></div>
<div class="abs stat" style="left:780px"><span class="ic"><svg width="24" height="24"><path d="M3 12l9-8 9 8M6 10v10h12V10" fill="none" stroke="#5c4a32" stroke-width="2"/></svg></span><div><em>Our propertys</em><strong>6587</strong></div></div>

<!-- listings -->
<section class="abs listing"></section>
<header class="abs sec-head" style="top:1253px">
  <h2 class="sec-title"><i class="l"></i>Property listing<i class="r"></i></h2>
  <p class="sec-desc">New homes from leading builders, each with a buyer's agent by your side at no extra cost.</p>
</header>

<article class="abs card" style="left:87px;top:1374px"><div class="photo" role="img" aria-label="Photo of a modern white villa" style="background:linear-gradient(180deg,#9fb0e0,#d6dbea 60%,#a9a9ae)"></div><span class="tag">$489</span><h3>Free buyer's agent</h3><p class="sub">Builder pays our fee</p><span class="spec" style="left:18px;top:258px">▦ 1800 sq ft</span><span class="spec" style="left:180px;top:258px">▭ Bedroom: 4</span><span class="spec" style="left:18px;top:290px">◡ Bathroom: 2</span><div class="foot"><span class="agent">☏ Contact Agent</span><span class="btn">♡</span><span class="btn">⋖</span></div></article>
<article class="abs card" style="left:438px;top:1374px"><div class="photo" role="img" aria-label="Photo of a stone family house" style="background:linear-gradient(180deg,#e4e9ec,#c9bca8 55%,#8fa875)"></div><span class="tag">$871</span><h3>Price negotiation</h3><p class="sub">Upgrades and incentives</p><span class="spec" style="left:18px;top:258px">▦ 1800 sq ft</span><span class="spec" style="left:180px;top:258px">▭ Bedroom: 4</span><span class="spec" style="left:18px;top:290px">◡ Bathroom: 2</span><div class="foot"><span class="agent">☏ Contact Agent</span><span class="btn">♡</span><span class="btn">⋖</span></div></article>
<article class="abs card" style="left:790px;top:1374px"><div class="photo" role="img" aria-label="Photo of a brick house with tiled roof" style="background:linear-gradient(180deg,#bcd9f0,#b8907c 50%,#dcae8c)"></div><span class="tag">$247</span><h3>Contract review</h3><p class="sub">We read the fine print</p><span class="spec" style="left:18px;top:258px">▦ 1800 sq ft</span><span class="spec" style="left:180px;top:258px">▭ Bedroom: 4</span><span class="spec" style="left:18px;top:290px">◡ Bathroom: 2</span><div class="foot"><span class="agent">☏ Contact Agent</span><span class="btn">♡</span><span class="btn">⋖</span></div></article>
<article class="abs card" style="left:87px;top:1805px"><div class="photo" role="img" aria-label="Photo of a modern house with red panels" style="background:linear-gradient(180deg,#c7d0db,#8a8a92 55%,#b89a80)"></div><span class="tag">$758</span><h3>Inspection support</h3><p class="sub">Checks at every stage</p><span class="spec" style="left:18px;top:258px">▦ 1800 sq ft</span><span class="spec" style="left:180px;top:258px">▭ Bedroom: 4</span><span class="spec" style="left:18px;top:290px">◡ Bathroom: 2</span><div class="foot"><span class="agent">☏ Contact Agent</span><span class="btn">♡</span><span class="btn">⋖</span></div></article>
<article class="abs card" style="left:438px;top:1805px"><div class="photo" role="img" aria-label="Photo of a white villa with pool" style="background:linear-gradient(180deg,#a8c6e6,#eeebe6 55%,#7fb3cc)"></div><span class="tag">$567</span><h3>Upgrade guidance</h3><p class="sub">Spend where it counts</p><span class="spec" style="left:18px;top:258px">▦ 1800 sq ft</span><span class="spec" style="left:180px;top:258px">▭ Bedroom: 4</span><span class="spec" style="left:18px;top:290px">◡ Bathroom: 2</span><div class="foot"><span class="agent">☏ Contact Agent</span><span class="btn">♡</span><span class="btn">⋖</span></div></article>
<article class="abs card" style="left:790px;top:1805px"><div class="photo" role="img" aria-label="Photo of a suburban house with garden" style="background:linear-gradient(180deg,#b3d2ef,#dcc6a8 50%,#86b070)"></div><span class="tag">$389</span><h3>Closing support</h3><p class="sub">With you to the keys</p><span class="spec" style="left:18px;top:258px">▦ 1800 sq ft</span><span class="spec" style="left:180px;top:258px">▭ Bedroom: 4</span><span class="spec" style="left:18px;top:290px">◡ Bathroom: 2</span><div class="foot"><span class="agent">☏ Contact Agent</span><span class="btn">♡</span><span class="btn">⋖</span></div></article>
<div class="abs view-more">VIEW MORE <span>→</span></div>

<!-- why choose -->
<header class="abs sec-head" style="top:2418px">
  <h2 class="sec-title"><i class="l"></i>Why chose our houses<i class="r"></i></h2>
  <p class="sec-desc">Watch the short video to see how a buyer's agent helps you buy new from any builder.</p>
</header>
<div class="abs video" role="img" aria-label="Video still of a bright modern living room"><span class="play"><svg width="14" height="14"><path d="M4 2l8 5-8 5z" fill="#fff"/></svg></span>Watch Video</div>
<h3 class="abs why-title">Your agent, at no extra cost</h3>
<p class="abs why-text">The builder's sales team works for the builder. Your buyer's agent works only for you, negotiates price and upgrades, reviews the contract and stays with you until closing.</p>
<div class="abs metric" style="left:630px"><span class="ic">♡</span><div><b>2471</b>People like</div></div>
<div class="abs metric" style="left:822px"><span class="ic">⋖</span><div><b>4274</b>People share</div></div>

<!-- testimonial -->
<section class="abs testimonial" role="img" aria-label="Light photo of a handshake over a desk"></section>
<div class="abs avatar" role="img" aria-label="Client portrait"></div>
<div class="abs t-name">SAM PORTER</div>
<div class="abs t-stars">★★★★★</div>
<p class="abs t-text">Having our own agent when buying from the builder saved us money on upgrades and gave us peace of mind.</p>
<div class="abs pager" style="top:3130px;color:#333"><span>⟵ PRE</span><span class="dots"><span></span><span class="on"></span><span></span></span><span>NEX ⟶</span></div>

<!-- footer -->
<footer class="abs footer"></footer>
<h4 class="abs f-title" style="left:87px;top:3250px">Don't miss the opportunity</h4>
<p class="abs f-text" style="left:87px;top:3290px;width:420px">Get new builder listings and buyer tips by email, with no cost and no obligation.</p>
<div class="abs subscribe"><span>Enter email address</span><i><svg width="16" height="16"><path d="M1 8l14-6-5 13-3-5z" fill="#333"/></svg></i></div>
<h4 class="abs f-title" style="left:612px;top:3250px">Feel free to contact us</h4>
<div class="abs contact" style="left:614px"><svg width="26" height="26" viewBox="0 0 24 24"><path d="M5 3h4l2 5-3 2a11 11 0 0 0 6 6l2-3 5 2v4a2 2 0 0 1-2 2A18 18 0 0 1 3 5a2 2 0 0 1 2-2z" fill="none" stroke="#444" stroke-width="1.5"/></svg><div><em>Call us</em><strong>245 555 0187</strong></div></div>
<div class="abs contact" style="left:825px"><svg width="30" height="22"><rect x="1" y="1" width="28" height="20" fill="none" stroke="#444" stroke-width="1.5"/><path d="M1 1l14 11L29 1" fill="none" stroke="#444" stroke-width="1.5"/></svg><div><em>Mail us</em><strong>hello@freshnestguide.com</strong></div></div>
<span class="abs social" style="left:614px"></span>
<span class="abs social" style="left:663px"></span>
<span class="abs social" style="left:713px"></span>
<span class="abs social" style="left:760px"></span>
<div class="abs bottom-bar">© 2016 <b>FRESH NEST BUILDER GUIDE</b> All Rights Reserved</div>

</body>
</html>
```